ultra-minimalist business card

front (black background, matte):

tarik b. hosseny
writer | photographer
get@tarikhosseny.com

back (white background, matte):

a picture speaks a thousand words;
a word draws a thousand pictures.

www.tarikhosseny.com

all text should be small (white or silver - as long as it shows against the black - on the front; black or gray - as long as it shows against the white - on the back).

feel free to get creative in terms of arrangement, alignment, and font type, but remember, the overall style is minimalist, so nothing too fancy, please.

thanks.

```html
<!DOCTYPE html>
<html lang="en">
<head>
<meta charset="utf-8">
<title>Tarik B. Hosseny — Business Card</title>
<link rel="stylesheet" href="https://fonts.googleapis.com/css2?family=Libre+Baskerville:wght@400;700&family=Montserrat:wght@400;500;600&display=swap">
<style>
  :root {
    --stage: #2a2b2c;
    --card-quote: #f4f4f2;
    --card-contact: #1d2023;
    --gray-name: #6d7175;
    --ink-dark: #26282a;
    --silver-light: #d4d7da;
    --ink-light: #eef0f1;
    --muted: #b9bdc1;
  }
  * { margin: 0; padding: 0; box-sizing: border-box; }
  html, body {
    width: 1200px;
    height: 1000px;
    overflow: hidden;
    background: var(--stage);
  }
  .stage {
    position: relative;
    width: 1200px;
    height: 1000px;
  }
  .card {
    position: absolute;
    width: 500px;
    height: 286px;
    box-shadow: 0 18px 40px rgba(0, 0, 0, 0.45);
  }
  /* quote side (back, white) */
  .card--quote {
    left: 80px;
    top: 250px;
    background: var(--card-quote);
  }
  .quote-card__name {
    position: absolute;
    left: 0;
    right: 0;
    top: 104px;
    text-align: center;
    font-family: "Libre Baskerville", serif;
    font-weight: 700;
    font-size: 22px;
    letter-spacing: 0.06em;
    color: var(--gray-name);
  }
  .quote-card__motto {
    position: absolute;
    right: 56px;
    bottom: 44px;
    text-align: right;
    font-family: "Montserrat", sans-serif;
    font-size: 12px;
    line-height: 1.45;
    letter-spacing: 0.02em;
    color: var(--ink-dark);
  }
  /* contact side (front, black) */
  .card--contact {
    left: 620px;
    top: 464px;
    background: var(--card-contact);
  }
  .contact-card__identity {
    position: absolute;
    right: 30px;
    top: 26px;
  }
  .contact-card__name {
    font-family: "Libre Baskerville", serif;
    font-weight: 700;
    font-size: 18px;
    color: var(--silver-light);
    letter-spacing: 0.01em;
  }
  .contact-card__role {
    margin-top: 2px;
    font-family: "Montserrat", sans-serif;
    font-size: 12px;
    letter-spacing: 0.08em;
    color: var(--muted);
  }
  .contact-card__details {
    position: absolute;
    left: 30px;
    bottom: 26px;
    font-family: "Montserrat", sans-serif;
    font-size: 12px;
    line-height: 1.6;
    color: var(--ink-light);
    list-style: none;
  }
  .contact-card__label {
    display: inline-block;
    width: 26px;
    font-weight: 600;
    color: var(--silver-light);
  }
</style>
</head>
<body>
  <main class="stage">
    <section class="card card--quote">
      <h1 class="quote-card__name">TARIK B. HOSSENY</h1>
      <p class="quote-card__motto">a picture speaks a thousand words;<br>a word draws a thousand pictures.</p>
    </section>

    <section class="card card--contact">
      <div class="contact-card__identity">
        <h2 class="contact-card__name">tarik b. hosseny</h2>
        <p class="contact-card__role">writer | photographer</p>
      </div>
      <ul class="contact-card__details">
        <li><span class="contact-card__label">E:</span>get@tarikhosseny.com</li>
        <li><span class="contact-card__label">W:</span>www.tarikhosseny.com</li>
      </ul>
    </section>
  </main>
</body>
</html>
```